Its time for a new website

We are at a point now where we are in desperate need of a new website. It was last updated 2006 but still looks like its 1995. We are looking for something eye catching to our clients but easy to navigate and add/remove photos of jobs/trucks and information. Our key business is the manufacture of fire appliances and resale of parts and equipment.

www.korlenrescue.com.au

Coding

Coded - Design and coding required

Number of Pages Required

5+ page

Requirements
Must have
• Logo

```html
<!DOCTYPE html>
<html lang="en">
<head>
<meta charset="utf-8">
<title>Korlen Rescue – Custom Firefighting Equipment</title>
<link href="https://fonts.googleapis.com/css2?family=Open+Sans:wght@400;600;700&family=Oswald:wght@400;500&display=swap" rel="stylesheet">
<style>
:root{
  --red:#d4262c;
  --blue:#1f6fb4;
  --ink:#333;
  --muted:#777;
  --footer:#2b2b2b;
  --footer-2:#222;
  --white:#fff;
}
*{box-sizing:border-box;margin:0;padding:0}
html,body{width:729px;height:1200px;overflow:hidden;background:var(--white)}
body{font-family:"Open Sans",Arial,sans-serif;color:var(--ink);font-size:9px;position:relative}
.topbar{height:70px;position:relative}
.brand{position:absolute;left:14px;top:14px;display:flex;align-items:center;gap:6px}
.brand-dot{width:36px;height:36px;border-radius:50%;background:var(--red)}
.brand-name{font-weight:700;font-size:13px;color:var(--red)}
.contact-line{position:absolute;right:14px;top:10px;display:flex;gap:18px;font-size:7px;color:var(--muted);align-items:center}
.contact-line span{display:flex;align-items:center;gap:4px}
.nav{position:absolute;top:70px;left:0;right:0;height:22px;background:var(--red);display:flex;padding-left:64px}
.nav a{color:var(--white);text-decoration:none;font-size:6.5px;font-weight:600;padding:0 9px;line-height:22px;white-space:nowrap}
.nav a.active{background:var(--blue)}
.hero{position:absolute;top:92px;left:0;width:729px;height:200px;background:linear-gradient(135deg,#3b4a5c 0%,#6b5a44 45%,#e0a048 60%,#4a3a30 100%)}
.hero-title{position:absolute;left:58px;top:86px;font-family:"Oswald",Arial,sans-serif;color:var(--white);font-size:19px;font-weight:500;letter-spacing:.5px}
.hero-sub{position:absolute;left:48px;top:112px;background:var(--red);color:var(--white);font-family:"Oswald",Arial,sans-serif;font-size:14px;padding:2px 14px}
.about{position:absolute;top:292px;left:0;width:729px;height:310px;background:linear-gradient(180deg,#eef1f4,#dfe5ea)}
.about-photo{position:absolute;left:0;top:40px;width:400px;height:250px;background:linear-gradient(160deg,#c9d3db 0%,#9aa6b1 45%,#b22a2e 70%,#8e9aa4 100%);opacity:.9}
.about-ribbon{position:absolute;right:0;top:0;width:350px;height:30px;background:var(--red);color:var(--white);font-family:"Oswald",Arial,sans-serif;font-size:16px;line-height:30px;padding-left:30px}
.about-ribbon::before{content:"";position:absolute;left:-20px;top:0;border-top:15px solid transparent;border-bottom:15px solid transparent;border-right:20px solid var(--red)}
.about-stripe{position:absolute;left:0;top:0;width:379px;height:30px;background:var(--blue)}
.about-text{position:absolute;left:412px;top:58px;width:290px;line-height:1.5}
.about-text .lead{font-size:8px;color:#555;margin-bottom:8px}
.about-text p{font-size:6.5px;color:var(--muted);margin-bottom:10px}
.btn{display:inline-block;background:var(--red);color:var(--white);font-size:6.5px;font-weight:600;padding:5px 10px}
.services{position:absolute;top:612px;left:0;width:729px;text-align:center}
.section-title{font-family:"Oswald",Arial,sans-serif;font-size:18px;color:var(--blue)}
.section-sub{font-size:7px;color:var(--muted);width:250px;margin:12px auto 0;line-height:1.5}
.grid{position:absolute;top:712px;left:61px;width:607px;height:192px}
.tile{position:absolute;overflow:hidden}
.tile-label{position:absolute;left:0;right:0;bottom:0;height:18px;background:rgba(31,111,180,.92);color:var(--white);font-size:8px;font-weight:600;line-height:18px;padding-left:8px}
.tile-label::after{content:"";position:absolute;right:7px;top:5px;width:8px;height:8px;border-radius:50%;background:var(--white)}
.news{position:absolute;top:945px;left:58px;width:300px}
.contact{position:absolute;top:945px;left:400px;width:270px}
.block-title{font-family:"Oswald",Arial,sans-serif;font-size:15px;color:var(--blue)}
.block-sub{font-size:7px;color:var(--muted);margin:4px 0 10px}
.news-item{display:flex;gap:8px;margin-top:12px}
.news-photo{width:40px;height:60px;background:linear-gradient(180deg,#5a2a2c,#c44a3a)}
.news-date{background:var(--red);color:var(--white);font-size:6px;padding:2px 5px;display:inline-block;margin-bottom:4px}
.news-item p{font-size:6px;color:var(--muted);line-height:1.5;width:150px}
.form{margin-top:10px;display:grid;grid-template-columns:1fr 1fr;gap:6px}
.field{height:16px;border:1px solid #ccc;font-size:6px;color:#999;padding:4px 6px}
.field.wide{grid-column:1/3;height:32px}
.submit{grid-column:2;justify-self:end;background:var(--blue);color:var(--white);font-size:6px;padding:4px 10px}
.footer{position:absolute;top:1125px;left:0;width:729px;height:75px;background:var(--footer)}
.footer-links{position:absolute;left:14px;top:14px;font-size:6.5px;color:#bbb}
.copyright{position:absolute;left:14px;top:28px;font-size:6px;color:#888}
.social{position:absolute;right:14px;top:12px;display:flex;gap:6px}
.social span{width:16px;height:16px;border-radius:50%;background:#555}
.footer-base{position:absolute;left:0;bottom:0;width:100%;height:28px;background:var(--footer-2)}
</style>
</head>
<body>
<header class="topbar">
  <div class="brand"><span class="brand-dot"></span><span class="brand-name">Korlen Rescue</span></div>
  <div class="contact-line">
    <span><svg width="7" height="9" viewBox="0 0 10 14"><path d="M5 0a5 5 0 0 0-5 5c0 4 5 9 5 9s5-5 5-9a5 5 0 0 0-5-5z" fill="#d4262c"/><circle cx="5" cy="5" r="2" fill="#fff"/></svg>Unit 4 Marden Road Hallow WA 6190 Western Australia</span>
    <span><svg width="8" height="8" viewBox="0 0 10 10"><path d="M2 0l2 2-1 2c1 1 2 2 3 3l2-1 2 2-2 2C4 10 0 6 0 2z" fill="#d4262c"/></svg>Phone +61 8 9000 4412 · Fax +61 8 9000 4413</span>
  </div>
  <nav class="nav">
    <a class="active">HOME</a><a>ABOUT US</a><a>PUMPERS</a><a>TANKERS</a><a>GRV/RESCUE</a><a>LIGHT TANKERS</a><a>TRAILERS</a><a>SLIP-ON UNITS</a><a>CONTACT US</a><a>NEW FOR 2015</a>
  </nav>
</header>

<section class="hero" role="img" aria-label="Welder cutting steel in the workshop with sparks flying">
  <h1 class="hero-title">WESTERN AUSTRALIA'S LEADING MANUFACTURER</h1>
  <div class="hero-sub">OF CUSTOM FIREFIGHTING EQUIPMENT</div>
</section>

<section class="about">
  <div class="about-stripe"></div>
  <div class="about-ribbon">ABOUT US</div>
  <div class="about-photo" role="img" aria-label="Red truck towing a silver tanker trailer"></div>
  <div class="about-text">
    <p class="lead">We design and build custom fire appliances in our own workshop, from first sketch to final handover, for crews across the state.</p>
    <p>Every vehicle is fitted, tested and certified on site, and our parts store keeps spares ready for fast dispatch.</p>
    <span class="btn">READ MORE</span>
  </div>
</section>

<section class="services">
  <h2 class="section-title">WHAT WE DO</h2>
  <p class="section-sub">Purpose-built appliances for rural, urban and industrial brigades across Western Australia.</p>
</section>
<div class="grid">
  <div class="tile" style="left:0;top:0;width:164px;height:192px;background:linear-gradient(160deg,#7a8ea0,#c0282d 55%,#6a6a6a)" role="img" aria-label="Red fire pumper truck"><div class="tile-label">Pumpers</div></div>
  <div class="tile" style="left:168px;top:0;width:218px;height:94px;background:linear-gradient(160deg,#8fb2cf,#c9ccd0 55%,#b8352f)" role="img" aria-label="Tanker truck"><div class="tile-label">Tankers</div></div>
  <div class="tile" style="left:390px;top:0;width:217px;height:94px;background:linear-gradient(160deg,#2d3b4c,#c7302c 60%,#4d4d4d)" role="img" aria-label="Fire and rescue truck"><div class="tile-label">GPA/Rescue</div></div>
  <div class="tile" style="left:168px;top:98px;width:218px;height:94px;background:linear-gradient(160deg,#9ab8d3,#e8e8e8 55%,#8a9099)" role="img" aria-label="White light tanker"><div class="tile-label">Light Tankers</div></div>
  <div class="tile" style="left:390px;top:98px;width:217px;height:94px;background:linear-gradient(160deg,#1d2a3c,#52647a 55%,#c08a4a)" role="img" aria-label="Slip-on firefighting unit at night"><div class="tile-label">Slip-on Units</div></div>
</div>

<section class="news">
  <h3 class="block-title">NEWS</h3>
  <p class="block-sub">Updates from the workshop floor and recent deliveries.</p>
  <div class="news-item">
    <div class="news-photo" role="img" aria-label="Fire appliance at a recent delivery"></div>
    <div><span class="news-date">Apr 12, 2015</span>
      <p>New light tanker delivered to a regional brigade this month, fitted with a high-flow pump and full rescue lockers. Read more about the build.</p></div>
  </div>
</section>

<section class="contact">
  <h3 class="block-title">CONTACT</h3>
  <div class="form">
    <div class="field">Name</div><div class="field">Email</div>
    <div class="field">Phone</div><div class="field">Service Enquiring</div>
    <div class="field wide">Message</div>
    <div class="submit">SUBMIT</div>
  </div>
</section>

<footer class="footer">
  <div class="footer-links">Home | About Us | Pumpers | Tankers | GPA/Rescue | Light Tankers | Trailers | Slip-on Units | Contact Us | New for 2015</div>
  <div class="copyright">Copyright © 2015 Korlen Rescue · www.korlenrescue.com.au · All rights reserved.</div>
  <div class="social"><span></span><span></span><span></span><span></span><span></span></div>
  <div class="footer-base"></div>
</footer>
</body>
</html>
```